We want to design total new business card and logo for Kestrel Building Services Ltd

Our company name Kestrel Building Services Ltd. Design new logo and business card , need hi-end luxury style art for architecture and construction industry. The card should simple but stylish. Our business focus on CONNECT tradesman to construction company, help marketing construction company tender oversea projects, managing franchise in construction sector, delivery amazing services to our client, so Logo should show the CONNECTION IDEA, CONNECTING PEOPLE, LUXURY. Visit our website for more information: kestrelhub.co.nz

Low design quality

Target Market(s)

Directors or managers

Industry/Entity Type

Construction Company

Contact Information for Business Card

Name, Title, Mobile, Email, Website

Font styles to use
Serif

Colors

Designer to choose colors to be used in the design.

Requirements
Must have
• Simple and luxury, connection icon
Nice to have
• Special materials, plastic card, look through,...
• Look new ideas.

```html
<!DOCTYPE html>
<html lang="en">
<head>
<meta charset="utf-8">
<title>Kestrel Building Services Ltd – Business Card</title>
<link rel="stylesheet" href="https://fonts.googleapis.com/css2?family=Open+Sans:wght@400;600;800&display=swap">
<style>
  :root {
    --backdrop: #e4e6e8;
    --card: #f3f3f1;
    --navy: #1d3f95;
    --sky: #2f9ccb;
    --teal: #3fb0c4;
    --ink: #2a2a2a;
    --white: #ffffff;
  }
  * { margin: 0; padding: 0; box-sizing: border-box; }
  html, body {
    width: 1200px; height: 971px; overflow: hidden;
    background: var(--backdrop);
    font-family: "Open Sans", Arial, sans-serif;
  }
  .canvas { position: relative; width: 1200px; height: 971px; }
  .card {
    position: absolute; left: 100px; top: 170px;
    width: 1000px; height: 630px;
    background: var(--card);
    border-radius: 28px;
    box-shadow: 0 14px 40px rgba(0,0,0,0.12);
    overflow: hidden;
  }
  .brand {
    position: absolute; left: 190px; top: 150px;
    display: flex; align-items: center; gap: 22px;
  }
  .brand-square { width: 34px; height: 34px; background: var(--navy); }
  .brand-name {
    font-weight: 800; font-size: 44px; color: var(--navy);
    letter-spacing: 0.5px;
  }
  .band-contact {
    position: absolute; left: 455px; top: 300px;
    width: 545px; height: 175px;
    background: var(--sky);
  }
  .band-person {
    position: absolute; left: 0; top: 365px;
    width: 450px; height: 135px;
    background: var(--navy);
  }
  .person {
    position: absolute; right: 42px; top: 36px; text-align: right;
  }
  .person-name { font-weight: 600; font-size: 31px; color: var(--teal); line-height: 1.1; }
  .person-title { font-size: 22px; color: var(--white); margin-top: 6px; }
  .contacts {
    position: absolute; left: 32px; top: 40px;
    list-style: none;
  }
  .contacts li {
    display: flex; align-items: center; gap: 12px;
    font-size: 23px; color: var(--white); line-height: 33px;
  }
  .contacts svg { width: 22px; height: 22px; flex: none; }
  .address {
    position: absolute; left: 0; right: 0; top: 540px;
    text-align: center; font-size: 24px; color: var(--ink);
  }
</style>
</head>
<body>
<main class="canvas">
  <section class="card">
    <div class="brand">
      <span class="brand-square"></span>
      <span class="brand-name">Kestrel Building Services Ltd</span>
    </div>

    <div class="band-contact">
      <ul class="contacts">
        <li>
          <svg viewBox="0 0 24 24"><path fill="#fff" d="M6.6 10.8a15.1 15.1 0 0 0 6.6 6.6l2.2-2.2a1 1 0 0 1 1-.25 11.4 11.4 0 0 0 3.6.57 1 1 0 0 1 1 1V20a1 1 0 0 1-1 1A17 17 0 0 1 3 4a1 1 0 0 1 1-1h3.5a1 1 0 0 1 1 1c0 1.25.2 2.45.57 3.57a1 1 0 0 1-.25 1z"/></svg>
          0800 555 014
        </li>
        <li>
          <svg viewBox="0 0 24 24"><rect x="2.5" y="5" width="19" height="14" fill="none" stroke="#fff" stroke-width="2"/><path d="M3 6l9 7 9-7" fill="none" stroke="#fff" stroke-width="2"/></svg>
          info@kestrelhub.co.nz
        </li>
        <li>
          <svg viewBox="0 0 24 24" fill="none" stroke="#fff" stroke-width="1.6"><circle cx="12" cy="12" r="9.5"/><ellipse cx="12" cy="12" rx="4" ry="9.5"/><path d="M2.5 12h19M4 7h16M4 17h16"/></svg>
          www.kestrelhub.co.nz
        </li>
      </ul>
    </div>

    <div class="band-person">
      <div class="person">
        <p class="person-name">Daniel Whitford</p>
        <p class="person-title">Managing Director</p>
      </div>
    </div>

    <p class="address">18 Tui Lane, Riverside, Auckland 2104, Newzealand</p>
  </section>
</main>
</body>
</html>
```